Dental FAQ/advert tri-fold for holistic family dentist

We are a dental clinic with a holistic emphasis. We are seeking new clients, mainly middle classed families. A tri-fold brochure that is both a useful dental FAQ to keep in the house and acts as an advertisement for our clinic. It will be mailed out. It needs to look clean, modern, somewhat minimalist, and I want it to follow the Orble design esthetic. website is willowcrestdentalcare.com
Updates

I just updated the pamphlet file with revised text! Thanks for the nice designs so far, keep em coming.

Target Market(s)

Young families. Upper middle classes.

Industry/Entity Type

Dental

Requirements
Must have
• Follows our logo and colours.

```html
<!DOCTYPE html>
<html lang="en">
<head>
<meta charset="utf-8">
<title>Willowcrest Dental Care – Frequently Asked Questions Brochure</title>
<link rel="stylesheet" href="https://fonts.googleapis.com/css2?family=Nunito+Sans:wght@300;400;600;700&display=swap">
<style>
  :root {
    --green: #2f9a45;
    --green-light: #4bb04a;
    --green-dark: #26803a;
    --heading-green: #2a8f3e;
    --ink: #333333;
    --white: #ffffff;
    --page: #ffffff;
    --edge: #e6e6e6;
    --photo-skin: #e8c3b5;
    --photo-lip: #d98a86;
    --photo-bg: #dfe7ec;
  }
  * { box-sizing: border-box; margin: 0; padding: 0; }
  html, body { width: 1200px; height: 933px; overflow: hidden; background: var(--page); }
  body { font-family: "Nunito Sans", Arial, sans-serif; color: var(--ink); }

  .brochure { position: relative; width: 1200px; height: 933px; background: var(--page); }

  /* ---------- left panel: FAQ ---------- */
  .faq-panel { position: absolute; left: 34px; top: 48px; width: 348px; }
  .faq-item { margin-bottom: 14px; }
  .faq-question { font-size: 12px; font-weight: 700; color: var(--heading-green); line-height: 19px; margin-bottom: 2px; }
  .faq-answer { font-size: 12.2px; line-height: 18.6px; text-align: justify; }

  .smile-photo {
    position: absolute; left: 0; top: 670px; width: 401px; height: 248px;
    background: radial-gradient(ellipse at 60% 50%, var(--photo-lip) 0%, var(--photo-skin) 45%, #f3ddd3 100%);
  }

  /* ---------- middle panel ---------- */
  .services-panel {
    position: absolute; left: 401px; top: 14px; width: 390px; height: 904px;
    background: linear-gradient(180deg, var(--green-light) 0%, var(--green) 55%, var(--green-dark) 100%);
    color: var(--white); text-align: center;
  }
  .welcome { margin-top: 38px; font-size: 17px; font-weight: 300; line-height: 22px; }
  .welcome strong { font-weight: 700; }
  .services-title { margin-top: 18px; font-size: 15.5px; font-weight: 700; }
  .services-list { margin-top: 8px; font-size: 13px; font-weight: 300; line-height: 19.7px; }

  .appointment { position: absolute; left: 0; right: 0; top: 424px; }
  .appointment-label { font-size: 13px; font-weight: 300; }
  .appointment-phone { margin-top: 4px; font-size: 35px; font-weight: 300; letter-spacing: 0.5px; }

  .clinic-block { position: absolute; left: 0; right: 0; top: 742px; }
  .clinic-name { display: inline-flex; align-items: center; gap: 7px; font-size: 16px; font-weight: 400; }
  .clinic-name .dot { width: 9px; height: 9px; border-radius: 50%; background: var(--white); }
  .clinic-contact { margin-top: 42px; font-size: 9.5px; font-weight: 300; line-height: 18px; }

  /* ---------- right panel: cover ---------- */
  .exam-photo {
    position: absolute; left: 791px; top: 14px; width: 396px; height: 333px;
    background: linear-gradient(135deg, var(--photo-bg) 0%, var(--photo-skin) 55%, #c9d4da 100%);
  }
  .title-band {
    position: absolute; left: 791px; top: 347px; width: 396px; height: 211px;
    background: linear-gradient(180deg, var(--green-light) 0%, var(--green-dark) 100%);
    color: var(--white); padding: 24px 0 0 28px;
  }
  .cover-title { font-size: 42px; font-weight: 300; line-height: 54px; }

  .cover-brand {
    position: absolute; left: 791px; top: 718px; width: 396px; text-align: center;
    color: var(--green);
  }
  .cover-brand .clinic-name { font-size: 24px; font-weight: 600; }
  .cover-brand .dot { width: 14px; height: 14px; background: var(--green); }
  .cover-url { position: absolute; left: 791px; top: 881px; width: 396px; text-align: center; font-size: 11px; color: var(--green); }
</style>
</head>
<body>
<main class="brochure">

  <section class="faq-panel">
    <article class="faq-item">
      <h3 class="faq-question">Do I need to have my wisdom teeth removed?</h3>
      <p class="faq-answer">While some people keep their wisdom teeth well into adulthood, wisdom teeth often don’t grow in properly and need to be removed before they become a problem. This usually happens between the ages of 16-22. Everybody is different and your dental provider will assess your teeth.</p>
    </article>
    <article class="faq-item">
      <h3 class="faq-question">What can cause a toothache?</h3>
      <p class="faq-answer">Toothaches are either caused by an irritated nerve within the tooth, or an infection surrounding the tooth. Usually over the counter pain medication like Ibuprofen can be used for temporary relief before your appointment. At your visit, our dentist will determine the exact cause of the problem and provide treatment options.</p>
    </article>
    <article class="faq-item">
      <h3 class="faq-question">What should I do if I knock a tooth out?</h3>
      <p class="faq-answer">Say sorry to the other person! Just kidding, if a tooth is knocked clear out, it can sometimes be re-implanted, if done within 30-60 minutes. Gently rinse the tooth off, and store it in a solution of milk or clean water and make your way to a dentist ASAP.</p>
    </article>
    <article class="faq-item">
      <h3 class="faq-question">Should I wear a mouth guard during recreational activities?</h3>
      <p class="faq-answer">Mouth guards should be used by anyone who plays contact sports such as hockey, football, boxing, soccer, basketball, and lacrosse. Your dentist can create a custom appliance that provides much more comfort and protection than a store-bought appliance.</p>
    </article>
    <article class="faq-item">
      <h3 class="faq-question">What’s the difference between teeth whitening in a dental office and store bought kits?</h3>
      <p class="faq-answer">A dental clinic can supply you with a custom fit tray to maximize your teeth whitening, as well as prescribe stronger formulations of the whitening solution for a longer lasting, whiter smile</p>
    </article>
  </section>

  <div class="smile-photo" role="img" aria-label="Photo of a bright white smile beside a dental mirror"></div>

  <section class="services-panel">
    <p class="welcome">We look forward to making your family<br>visit with us <strong>exceptional</strong></p>
    <h2 class="services-title">Our Services</h2>
    <p class="services-list">
      Composite Restorations | Crowns | Dental Extractions<br>
      Digital X-rays | Emergencies | Fluoride - Free<br>
      Free - Baby Sitting | Implants And Bridges<br>
      Laser Dentistry | Orthodontics | Preventative Care<br>
      Root Canal Therapy | Teeth Whitening<br>
      Veneers And Bonding | Wisdom Teeth Removal
    </p>

    <div class="appointment">
      <p class="appointment-label">Make an appointment today</p>
      <p class="appointment-phone">403-555-0148</p>
    </div>

    <div class="clinic-block">
      <p class="clinic-name"><span class="dot"></span>Willowcrest Dental Care</p>
      <p class="clinic-contact">
        Suite 210, 4415 Harbour Ridge Way SE, Calgary AB, T2X 4K9<br>
        email : admin@willowcrestdentalcare.com<br>
        www.willowcrestdentalcare.com<br>
        Phone No. : 403-555-0148
      </p>
    </div>
  </section>

  <div class="exam-photo" role="img" aria-label="Photo of a patient having a dental examination with mirror and probe"></div>

  <section class="title-band">
    <h1 class="cover-title">Frequently Asked<br>Questions For<br>Your Dentist</h1>
  </section>

  <div class="cover-brand">
    <p class="clinic-name"><span class="dot"></span>Willowcrest Dental Care</p>
  </div>
  <p class="cover-url">www.willowcrestdentalcare.com</p>

</main>
</body>
</html>
```